Custom Cabinet Shop Needs a website design

Hi,
We need a website for a Custom Cabinet Shop and Cabinet parts manufacturing business.
The business has two sides to it. One side provides custom Kitchens, vanities, entertainment units, offices and what not to homeowners and contractors.
The 2nd side of the business provides built to order cabinet boxes and other parts required to put together a project to other cabinet shops, small contractors looking to install there own cabinets.
Website will need a Gallery to display work.
Color scheme to go well with logo.
current website is www.brindlewoodcustomcabinets.com
being changed to www.brindlewood.ca
Logo Included in attached files.
Tagline "Millwork with Flare"
Mission Statement "Our passion is to deliver inspired cabinetry solutions to suit all your needs, supported by our phenomenal star class customer service"
The website should convey quality and professionalism.
Thank you.
Homeowners/ Contractors
Entertainment
Coded - Design and coding required
1 page

```html
<!DOCTYPE html>
<html lang="en">
<head>
<meta charset="utf-8">
<title>Brindlewood Custom Cabinets</title>
<link rel="stylesheet" href="https://fonts.googleapis.com/css2?family=Open+Sans:ital,wght@0,300;0,400;0,600;0,700;1,400&family=Ubuntu:wght@500;700&display=swap">
<style>
:root{
  --orange:#f26522;
  --orange-dark:#d9541a;
  --ink:#2b2b2b;
  --topbar:#2e2e2e;
  --header-top:#ffffff;
  --header-bottom:#e4e4e4;
  --nav-active:#9a9a9a;
  --text-grey:#6d6d6d;
  --footer:#333333;
  --footer-bottom:#262626;
  --footer-text:#a8a8a8;
  --line:#4a4a4a;
  --white:#ffffff;
}
*{box-sizing:border-box;margin:0;padding:0}
html,body{width:1200px;height:3000px;overflow:hidden}
body{font-family:"Open Sans",Arial,sans-serif;color:var(--ink);background:var(--white);position:relative}

/* top bar */
.topbar{position:absolute;left:0;top:0;width:1200px;height:30px;background:var(--topbar)}
.topbar .social{position:absolute;left:96px;top:7px;display:flex;gap:18px}
.topbar .social span{width:16px;height:16px;border-radius:50%;background:#bdbdbd;display:block}
.search{position:absolute;left:910px;top:5px;width:184px;height:20px;border:1px solid #cfcfcf;border-radius:10px;color:#ddd;font-size:10px;font-style:italic;padding:2px 10px}
.search svg{position:absolute;right:8px;top:3px}

/* header */
.header{position:absolute;left:0;top:30px;width:1200px;height:126px;background:linear-gradient(var(--header-top),var(--header-bottom));border-bottom:5px solid var(--orange)}
.brand{position:absolute;left:96px;top:40px;display:flex;align-items:center;gap:14px}
.brand .mark{width:44px;height:44px;background:var(--orange)}
.brand .name{font-family:"Open Sans",sans-serif;font-weight:700;font-size:30px;color:var(--ink);letter-spacing:1px}
.nav{position:absolute;left:694px;top:0;display:flex;height:121px}
.nav a{display:block;text-decoration:none;color:#4a4a4a;font-size:15px;line-height:121px;padding:0 16px}
.nav a.active{background:var(--nav-active);color:var(--white);font-weight:600;width:72px;padding:0;text-align:center}

/* hero */
.hero{position:absolute;left:0;top:160px;width:1200px;height:494px;background:linear-gradient(120deg,#1f2226 0%,#3a2f27 45%,#5a4434 70%,#2a2420 100%)}
.hero-title{position:absolute;left:0;top:342px;width:1200px;text-align:center;color:var(--white);font-weight:300;font-size:40px;line-height:46px}
.hero-sub{position:absolute;left:260px;top:444px;width:680px;text-align:center;color:#eee;font-size:17px;line-height:24px}
.arrow{position:absolute;top:382px;width:48px;height:48px;background:var(--orange)}
.arrow svg{position:absolute;left:14px;top:14px}
.dots{position:absolute;left:568px;top:624px;display:flex;gap:6px}
.dots span{width:16px;height:16px;border-radius:50%;background:#9a9a9a;display:block}

/* welcome */
.welcome{position:absolute;left:0;top:654px;width:1200px;height:426px;background:var(--orange)}
.welcome .kicker{position:absolute;left:100px;top:68px;color:var(--white);font-size:27px;font-weight:300;line-height:30px}
.welcome .title{position:absolute;left:100px;top:100px;width:460px;white-space:nowrap;color:var(--white);font-size:29px;font-weight:400;line-height:36px}
.welcome .photo{position:absolute;left:100px;top:156px;width:454px;height:236px;border:4px solid var(--white);background:linear-gradient(100deg,#6b5a4c,#2a2524 45%,#d9d4cc 80%,#b9b1a6)}
.about-title{position:absolute;left:588px;top:76px;color:var(--white);font-size:36px;font-weight:700;line-height:40px}
.about-sub{position:absolute;left:588px;top:118px;color:var(--white);font-size:14px;font-weight:700;line-height:18px}
.about-text{position:absolute;left:588px;top:150px;width:512px;color:var(--white);font-size:11px;line-height:18px}
.btn-read{position:absolute;left:588px;top:350px;width:138px;height:44px;background:var(--white);color:var(--orange);font-weight:600;font-size:15px;line-height:44px;text-align:center}

/* services */
.service{position:absolute;top:1126px;width:318px}
.service .head{display:flex;align-items:flex-start;gap:14px;height:50px}
.service .head h3{font-family:"Ubuntu",sans-serif;font-weight:700;font-size:19px;line-height:20px;color:var(--ink)}
.service .img{position:absolute;left:0;top:78px;width:318px;height:210px}
.service p{position:absolute;left:0;top:306px;width:318px;font-size:12px;line-height:17px;color:var(--text-grey);font-weight:600}
.service .more{position:absolute;left:0;top:402px;height:44px;border-left:1px solid #ddd;padding-left:12px;font-size:13px;color:var(--orange);line-height:44px;display:flex;align-items:center;gap:10px}
.more i{display:block;width:18px;height:18px;border:1px solid #888;border-radius:50%;position:relative}
.more i::after{content:"";position:absolute;left:6px;top:5px;border-left:5px solid #888;border-top:3px solid transparent;border-bottom:3px solid transparent}
.link-badge{position:absolute;left:114px;top:62px;width:88px;height:88px;border-radius:50%;background:var(--orange)}

/* testimonials */
.testimonials{position:absolute;left:0;top:1624px;width:1200px;height:432px;background:linear-gradient(100deg,#2b2623,#3e3530 40%,#2a2624 70%,#4a4542)}
.testimonials h2{position:absolute;left:0;top:56px;width:1200px;text-align:center;color:var(--white);font-weight:400;font-size:27px}
.quote{position:absolute;left:568px;top:130px}
.testimonials h4{position:absolute;left:0;top:200px;width:1200px;text-align:center;color:var(--white);font-weight:400;font-size:24px}
.testimonials p{position:absolute;left:110px;top:248px;width:980px;text-align:center;color:var(--white);font-size:12.5px;line-height:17px}
.see-all{position:absolute;left:546px;top:354px;width:106px;height:42px;border:2px solid #ddd;color:var(--white);font-size:12px;line-height:38px;text-align:center;font-weight:600}

/* gallery */
.gallery-title{position:absolute;left:0;top:2106px;width:1200px;text-align:center;font-size:27px;font-weight:400;color:var(--ink)}
.gallery{position:absolute;left:98px;top:2170px;width:1002px;height:454px;display:grid;grid-template-columns:repeat(5,1fr);grid-template-rows:repeat(3,1fr)}
.gallery div{width:100%;height:100%}

/* footer */
.footer-rule{position:absolute;left:0;top:2690px;width:1200px;height:14px;background:#e6e6e6}
.footer{position:absolute;left:0;top:2704px;width:1200px;height:246px;background:var(--footer)}
.footer .brand-f{position:absolute;left:100px;top:18px;display:flex;align-items:center;gap:10px}
.brand-f .mark{width:30px;height:30px;background:var(--white)}
.brand-f .name{color:var(--white);font-weight:700;font-size:20px;letter-spacing:1px}
.footer .blurb{position:absolute;left:100px;top:76px;width:210px;font-style:italic;font-size:11px;line-height:15px;color:var(--footer-text)}
.footer h5{position:absolute;top:34px;color:var(--white);font-size:11px;font-weight:700}
.posts{position:absolute;left:354px;top:66px;width:200px;list-style:none}
.posts li{font-size:10.5px;color:#ddd;height:34px;line-height:34px;border-bottom:1px solid var(--line)}
.tweets{position:absolute;left:614px;top:70px;width:200px;font-size:10.5px;line-height:16px;color:var(--footer-text)}
.tweets b{color:#ddd;font-weight:400}
.tweets p{margin-bottom:24px}
.photos{position:absolute;left:872px;top:78px;display:grid;grid-template-columns:repeat(4,52px);gap:6px}
.photos span{width:52px;height:52px;background:#e9e9e9;display:block}
.footer-bottom{position:absolute;left:0;top:2950px;width:1200px;height:50px;background:var(--footer-bottom)}
.copyright{position:absolute;left:110px;top:18px;font-size:10px;color:#999}
.tip{position:absolute;left:928px;top:-8px;background:#111;color:#ccc;font-size:9px;padding:2px 6px}
.f-social{position:absolute;left:946px;top:18px;display:flex;gap:22px}
.f-social span{width:12px;height:12px;border-radius:50%;background:#6a6a6a;display:block}
</style>
</head>
<body>

<div class="topbar">
  <div class="social"><span></span><span></span><span></span><span></span><span></span></div>
  <div class="search">Search
    <svg width="14" height="14" viewBox="0 0 14 14"><circle cx="6" cy="6" r="4.5" fill="none" stroke="#ddd" stroke-width="1.5"/><line x1="9.3" y1="9.3" x2="13" y2="13" stroke="#ddd" stroke-width="1.8"/></svg>
  </div>
</div>

<header class="header">
  <div class="brand"><span class="mark"></span><span class="name">BRINDLEWOOD</span></div>
  <nav class="nav">
    <a class="active">Home</a><a>Gallery</a><a>Services</a><a>Warranty</a><a>Contact</a>
  </nav>
</header>

<section class="hero" role="img" aria-label="Photograph of a dark custom kitchen with a wooden island bar, stools and pendant lights">
</section>
<div class="hero-title">OUR BEST SERVICES<br>FOR BEST CLIENTS</div>
<div class="hero-sub">Emergent eradicate, medical supplies assistance, education pride challenges of our times.</div>
<div class="arrow" style="left:0"><svg width="20" height="20" viewBox="0 0 20 20"><polyline points="13,3 6,10 13,17" fill="none" stroke="#fff" stroke-width="3"/></svg></div>
<div class="arrow" style="left:1152px"><svg width="20" height="20" viewBox="0 0 20 20"><polyline points="7,3 14,10 7,17" fill="none" stroke="#fff" stroke-width="3"/></svg></div>
<div class="dots"><span></span><span></span><span></span></div>

<section class="welcome">
  <div class="kicker">WELCOME TO</div>
  <div class="title">Brindlewood Custom Cabinets</div>
  <div class="photo" role="img" aria-label="Photograph of a bedroom with dark built-in cabinetry around a fireplace"></div>
  <div class="about-title">ABOUT</div>
  <div class="about-sub">LOREM IPSUM DOLOR SIT AMET CONSE</div>
  <p class="about-text">Lorem ipsum dolor sit amet conse ctetur adipisicing elit, sed do eiusmod tempor incididunt ut labore et dolore magna aliqua. Ut enim ad minim veniam, quis nostrud exercitation ullamco laboris nisi ut aliquip ex ea commodo consequat. Duis aute irure dolor in reprehenderit in voluptate velit esse cillum dolore eu fugiat nulla pariatur. Excepteur sint occaecat cupidatat non proident, sunt in culpa qui officia deserunt mollit anim id est laborum. Lorem ipsum dolor sit amet conse ctetur adipisicing elit, sed do eiusmod tempor incididunt ut labore et dolore magna aliqua. Ut enim ad minim veniam, quis nostrud exercitation ullamco laboris nisi ut aliquip ex ea commodo consequat. Duis aute irure dolor in reprehenderit in voluptate velit esse cillum dolore eu fugiat nulla pariatur. Excepteur sint occaecat cupidatat non proident, sunt in culpa qui officia deserunt mollit anim id est laborum.</p>
  <div class="btn-read">READ MORE</div>
</section>

<article class="service" style="left:98px">
  <div class="head">
    <svg width="26" height="38" viewBox="0 0 26 38"><rect x="4" y="2" width="18" height="16" rx="3" fill="#f26522"/><rect x="2" y="18" width="22" height="6" fill="#f26522"/><rect x="4" y="24" width="4" height="12" fill="#f26522"/><rect x="18" y="24" width="4" height="12" fill="#f26522"/></svg>
    <h3>Kitchen &amp; Bath<br>Design</h3>
  </div>
  <div class="img" role="img" aria-label="Photograph of a dark modern bathroom vanity" style="background:linear-gradient(135deg,#3c3c3c,#6a6a6a 50%,#2c2c2c)">
    <div class="link-badge">
      <svg width="88" height="88" viewBox="0 0 88 88"><g fill="none" stroke="#fff" stroke-width="5"><circle cx="37" cy="37" r="8"/><circle cx="51" cy="51" r="8"/><line x1="42" y1="42" x2="46" y2="46"/></g></svg>
    </div>
  </div>
  <p>Lorem ipsum dolor sit amet, consectetur adipisicing elit, sed do eiusmod tempor incididunt ut labore et dolore magna aliqua. Ut enim ad minim veniam, quis nostrud exercitaullamco laboris nisi ut aliquip.</p>
  <div class="more">more <i></i></div>
</article>

<article class="service" style="left:440px">
  <div class="head">
    <svg width="30" height="38" viewBox="0 0 30 38"><polygon points="7,2 23,2 28,18 2,18" fill="#f26522"/><rect x="13" y="18" width="4" height="14" fill="#f26522"/><rect x="6" y="32" width="18" height="4" fill="#f26522"/></svg>
    <h3>New &amp; Existing Furniture<br>Arrangements</h3>
  </div>
  <div class="img" role="img" aria-label="Photograph of a bright white kitchen with a glossy island and wood floor" style="background:linear-gradient(180deg,#e6e4e0,#f4f3f1 45%,#8a5a34 85%,#6b4426)"></div>
  <p>Lorem ipsum dolor sit amet, consectetur adipisicing elit, sed do eiusmod tempor incididunt ut labore et dolore magna aliqua. Ut enim ad minim veniam, quis nostrud exercitaullamco laboris nisi ut aliquip.</p>
  <div class="more">more <i></i></div>
</article>

<article class="service" style="left:782px">
  <div class="head">
    <svg width="38" height="32" viewBox="0 0 38 32"><circle cx="19" cy="8" r="6" fill="#f26522"/><circle cx="7" cy="12" r="4.5" fill="#f26522"/><circle cx="31" cy="12" r="4.5" fill="#f26522"/><path d="M9 30 Q19 10 29 30Z" fill="#f26522"/><path d="M0 30 Q7 16 13 30Z" fill="#f26522"/><path d="M25 30 Q31 16 38 30Z" fill="#f26522"/></svg>
    <h3>Interior Structural<br>Consulting</h3>
  </div>
  <div class="img" role="img" aria-label="Photograph of a sunlit living room with a red lounge chair by large windows" style="background:linear-gradient(180deg,#9fc2de,#d8d6cf 50%,#b9a58e 80%,#a23a2a)"></div>
  <p>Lorem ipsum dolor sit amet, consectetur adipisicing elit, sed do eiusmod tempor incididunt ut labore et dolore magna aliqua. Ut enim ad minim veniam, quis nostrud exercitaullamco laboris nisi ut aliquip.</p>
  <div class="more">more <i></i></div>
</article>

<section class="testimonials" role="img" aria-label="Darkened photograph of a kitchen with granite counters and bar chairs">
  <h2>TESTIMONIALS</h2>
  <svg class="quote" width="64" height="56" viewBox="0 0 64 56"><path d="M4 52V30C4 14 12 6 26 4v8c-8 2-12 8-12 16h12v24Z M36 52V30C36 14 44 6 58 4v8c-8 2-12 8-12 16h12v24Z" fill="#fff"/></svg>
  <h4>EU FUGIAT NULLA PARIATUR</h4>
  <p>Lorem ipsum dolor sit amet conse ctetur adipisicing elit, sed do eiusmod tempor incididunt ut labore et dolore magna aliqua. Ut enim ad minim veniam, quis nostrud exercitation ullamco laboris nisi ut aliquip ex ea commodo consequat. Duis aute irure dolor in reprehenderit in voluptate velit esse cillum dolore eu fugiat nulla pariatur. Excepteur sint occaecat cupidatat non proident.</p>
  <div class="see-all">SEE ALL</div>
</section>

<h2 class="gallery-title">GALLERY</h2>
<section class="gallery" role="img" aria-label="Grid of fifteen photographs of finished custom cabinetry and furnished rooms">
  <div style="background:linear-gradient(135deg,#2a2a2a,#5a5a5a)"></div>
  <div style="background:linear-gradient(135deg,#d8d3cc,#3b3532)"></div>
  <div style="background:linear-gradient(135deg,#8c5a36,#e8e2d8)"></div>
  <div style="background:linear-gradient(135deg,#c9a57c,#f0ebe3)"></div>
  <div style="background:linear-gradient(135deg,#bfc3c6,#7b756e)"></div>
  <div style="background:linear-gradient(135deg,#e9e9e9,#5a5a5a)"></div>
  <div style="background:linear-gradient(135deg,#a9a39b,#dcd7cf)"></div>
  <div style="background:linear-gradient(135deg,#6b4a35,#c2b3a0)"></div>
  <div style="background:linear-gradient(135deg,#1f1f1f,#f2f2f2)"></div>
  <div style="background:linear-gradient(135deg,#7d8e7a,#e6e3de)"></div>
  <div style="background:linear-gradient(135deg,#8e7356,#f1ede6)"></div>
  <div style="background:linear-gradient(135deg,#4e4038,#b59d84)"></div>
  <div style="background:linear-gradient(135deg,#2c2c2c,#9a9a9a)"></div>
  <div style="background:linear-gradient(135deg,#3e3a36,#c6b8a6)"></div>
  <div style="background:linear-gradient(135deg,#f4f4f4,#8a8a8a)"></div>
</section>

<div class="footer-rule"></div>
<footer class="footer">
  <div class="brand-f"><span class="mark"></span><span class="name">BRINDLEWOOD</span></div>
  <p class="blurb">Lorem ipsum ex vix illud nonummy, novum tation et his. At vix scriptaee patrioque scribentur, ar pro fugit eris verterem molestiae, sed et vivendo ad. Lorem ipsum ex vix illud nonummy, novum tation et his. At vix scripta patrioque scribentur...</p>
  <h5 style="left:354px">RECENT POSTS</h5>
  <ul class="posts">
    <li>Voluptas Sadips Ipsums Dolors Untra</li>
    <li>Fugiats Litora Ultrices Ante Auctor</li>
    <li>Sapien Litora Dolores Ultrices</li>
    <li>Nemis Fugiats Voluptas Dolores Uns</li>
  </ul>
  <h5 style="left:614px">CHIRPER</h5>
  <div class="tweets">
    <p><b>@marlowe</b> What an awesome theme! We love it, tons of options and great design, thank you! <b>12 minutes ago</b></p>
    <p><b>@marlowe</b> you've got to check this one out, very cool looking! <b>25 minutes ago</b></p>
  </div>
  <h5 style="left:872px">SNAPREEL</h5>
  <div class="photos"><span></span><span></span><span></span><span></span><span></span><span></span><span></span><span></span></div>
</footer>
<div class="footer-bottom">
  <div class="copyright">Copyright 2015 &nbsp;|&nbsp; All Rights Reserved &nbsp;|&nbsp; Powered by Pressfield</div>
  <div class="tip">Friendbook</div>
  <div class="f-social"><span></span><span></span><span></span><span></span><span></span></div>
</div>

</body>
</html>
```